Website design for Harbourline Bag printing specialist

We need an overhaul of our website front end design. We need a new look and a modern take on the products we sell and service we offer. We sell plain stock in a variety of bag types and offer a printing service of customers branding and logos. Customers request online quotes and this facility must be an easy one step process for users. Our logo is currently green and orange and we are not really looking for re branding at this stage. The final design must communicate that we are the leading printing specialist throughout the country, have been in operation for 15 years and have a vast amount of experience and expertise. The design must instantly show the products available and the ability to request a quote for the desired product.

Target Market(s)

Trade shows, retailers, dentists, food suppliers. wine makers etc etc and anyone that uses carry bags

Industry/Entity Type

Screen Printing

Number of Pages Required

5+ page

Font styles to use
Serif
Sans Serif

Colors

Designer to choose colors to be used in the design.

Requirements
Must have
• Our home page featuring all the products as selectable entities and a short description of what each bag type is when the user hovers over the image.
• Then the product landing pages must show different sizes of that product type. On each page there must be a quick quote button that goes to the quote screen with the features and information to select or include for a quote to be processed. The logo is green and orange and still should have this present but happy to move away from this on the website pages in general.I have so many product pictures and unable to upload them all here. The categories for products are as follows:
• Kraft Paper Bags
• Laminated bags
• Non-woven bags
• Calico bags
• Wine bags
• Florist bags
• Plastic Bags
• Printed Bags
• Gift Boxes
• Tissue paper
• Wrapping Paper
• Custom Bags and Boxes
• There also needs to be a gallery page that showcases work we have done. The ability to have a description for each photo in the gallery would be great.
• A general bag size page would be great and one content page that is about us and another for contact us.
• A free sample button so a user can request a sample. Phone number must be included on this page and unable to submit with a valid phone number.
• Our phone number should be prominent.
• A search feature please.
Nice to have
• Fonts should be in keeping with the design of the website
Should not have
• I dont want users having to scroll too far down to find information. The icons of the bags on the home screen should almost appear on one screen.
• I can upload all my content and pictures so no need to get them from me. I really want your look and feel and design layout that i can then work from.

```html
<!DOCTYPE html>
<html lang="en">
<head>
<meta charset="utf-8">
<title>Harbourline Bag – Bag Printing Specialist</title>
<link href="https://fonts.googleapis.com/css2?family=Bai+Jamjuree:wght@500;600;700&family=Open+Sans:wght@400;600;700&display=swap" rel="stylesheet">
<style>
:root{
  --green:#6cb833;
  --green-dark:#0f4a1c;
  --orange:#f26a1b;
  --orange-deep:#e8401a;
  --ink:#1a1a1a;
  --grey-text:#444;
  --line:#cfcfcf;
  --footer-bg:#eeeeee;
  --white:#ffffff;
  --head:"Bai Jamjuree",sans-serif;
  --body:"Open Sans",sans-serif;
}
*{margin:0;padding:0;box-sizing:border-box}
html,body{width:1200px;height:2875px;overflow:hidden;background:var(--white)}
body{position:relative;font-family:var(--body);color:var(--ink)}

/* header */
.site-header{position:absolute;left:0;top:0;width:1200px;height:112px;background:var(--white)}
.brand{position:absolute;left:163px;top:28px;font-family:var(--head);font-weight:700;font-size:40px;color:var(--green-dark);line-height:1;display:flex;align-items:center;gap:10px}
.brand-dot{width:18px;height:18px;border-radius:50%;background:var(--green)}
.quote-btn{position:absolute;left:704px;top:12px;width:139px;height:44px;border-radius:22px;background:var(--green-dark);color:var(--white);font-family:var(--head);font-weight:600;font-size:17px;display:flex;align-items:center;justify-content:center}
.phone{position:absolute;left:862px;top:14px;display:flex;align-items:center;gap:8px;font-family:var(--head);font-weight:700;font-size:25px;color:var(--ink)}
.main-nav{position:absolute;right:96px;top:68px;display:flex;gap:42px;font-family:var(--body);font-size:20px;color:var(--ink)}

/* hero */
.hero{position:absolute;left:0;top:112px;width:1200px;height:660px;background:
  linear-gradient(180deg,rgba(0,0,0,0) 0%,rgba(0,0,0,0) 75%,#c9a780 79%,#dcc2a0 100%),
  radial-gradient(ellipse at 70% 35%,#d4ecb0 0%,#8cc75a 38%,#4f9a2a 75%,#3a7d20 100%)}
.hero-products{position:absolute;left:760px;top:182px;width:310px;height:393px;border-radius:18px;background:linear-gradient(160deg,#2f8f3a 0%,#b98862 55%,#8a6545 100%);opacity:.85}
.hero-title{position:absolute;left:152px;top:286px;font-family:var(--head);font-weight:700;font-size:40px;line-height:1.1;color:var(--green-dark);white-space:nowrap}
.hero-title span{color:var(--orange)}
.hero-sub{position:absolute;left:158px;top:345px;width:520px;font-size:20px;line-height:30px;color:var(--green-dark)}
.search{position:absolute;left:155px;top:424px;width:446px;height:51px;border-radius:26px;background:var(--white);border:2px solid #d8d8d8;display:flex;align-items:center;padding-left:20px;gap:12px;font-size:15px;color:#888}
.dots{position:absolute;left:548px;top:650px;display:flex;gap:10px}
.dots i{width:19px;height:19px;border-radius:50%;border:2px solid #444;display:block}
.dots i.on{background:#444}
.hero-curve{position:absolute;left:0;top:690px}

/* categories */
.section-title{position:absolute;width:1200px;left:0;text-align:center;font-family:var(--head);font-weight:600;font-size:33px}
.cat-title{top:768px;color:var(--orange)}
.cat-card{position:absolute;width:221px;height:261px;background:var(--white);border:2px solid #dcdcdc;overflow:hidden}
.cat-photo{position:absolute;left:40px;top:22px;width:140px;height:160px;border-radius:6px}
.cat-label{position:absolute;left:0;bottom:0;width:100%;height:74px;border-radius:50% 50% 0 0/22px 22px 0 0;color:var(--white);font-family:var(--head);font-weight:600;font-size:19px;display:flex;align-items:flex-end;justify-content:center;padding-bottom:14px}
.is-green{background:var(--green)}
.is-orange{background:var(--orange)}
.arrow{position:absolute;top:984px}

/* about */
.about-shape{position:absolute;left:0;top:1210px}
.about-title{top:1278px;color:var(--white);font-size:35px}
.about-text{position:absolute;left:245px;width:710px;text-align:center;color:var(--white);font-size:18.5px;line-height:27px}
.pill-btn{position:absolute;height:51px;border-radius:26px;background:var(--green);color:var(--white);font-family:var(--head);font-weight:600;font-size:18px;display:flex;align-items:center;justify-content:center}

/* gallery */
.gallery-title{top:1726px;color:var(--ink)}
.g-card{position:absolute;background:var(--white);border:2px solid var(--line);border-radius:4px}
.g-title{font-family:var(--head);font-weight:700;font-size:21px;color:var(--orange)}
.g-text{font-size:13px;line-height:19px;color:var(--grey-text)}
.g-wide .g-title{position:absolute;left:42px;top:70px}
.g-wide .g-text{position:absolute;left:42px;top:100px;width:190px}
.g-wide .g-photo{position:absolute;right:50px;top:12px;width:110px;height:230px;border-radius:8px}
.g-small .g-photo{position:absolute;left:75px;top:22px;width:115px;height:172px;border-radius:8px}
.g-small .g-title{position:absolute;left:0;width:100%;text-align:center;top:208px}
.g-small .g-text{position:absolute;left:20px;width:225px;text-align:center;top:240px}

/* footer */
.site-footer{position:absolute;left:0;top:2496px;width:1200px;height:309px;background:var(--footer-bg);border-top:3px solid #dadada}
.footer-brand{position:absolute;left:173px;top:2572px;width:200px;font-family:var(--head);font-weight:700;font-size:32px;line-height:36px;color:var(--green-dark)}
.f-col{position:absolute;top:2553px}
.f-col h4{font-family:var(--body);font-weight:700;font-size:16px;color:var(--ink);margin-bottom:14px}
.f-col li{list-style:none;font-size:14.5px;line-height:27px;color:#333}
.f-contact li{line-height:34px;font-size:15px}
.social li{display:flex;align-items:center;gap:10px;line-height:34px}
.social i{width:22px;height:22px;border-radius:50%;background:#2a6fb0;display:block}
.copyright{position:absolute;left:0;top:2805px;width:1200px;height:70px;background:var(--footer-bg);border-top:1px solid #d4d4d4;text-align:center;padding-top:24px;font-size:14.5px;color:#444}
</style>
</head>
<body>

<header class="site-header">
  <div class="brand"><span>Harbourline Bag</span><span class="brand-dot"></span></div>
  <div class="quote-btn">Online Quote</div>
  <div class="phone">
    <svg width="22" height="22" viewBox="0 0 24 24"><path fill="#f26a1b" d="M6.6 10.8a15.1 15.1 0 0 0 6.6 6.6l2.2-2.2c.3-.3.7-.4 1-.2 1.1.4 2.3.6 3.6.6.6 0 1 .4 1 1V20c0 .6-.4 1-1 1A17 17 0 0 1 3 4c0-.6.4-1 1-1h3.5c.6 0 1 .4 1 1 0 1.3.2 2.5.6 3.6.1.3 0 .7-.2 1z"/></svg>
    1300 482 615
  </div>
  <nav class="main-nav"><span>Home</span><span>About us</span><span>Gallery</span><span>Bag Size</span><span>Contact us</span></nav>
</header>

<section class="hero" role="img" aria-label="Soft green bokeh background over a wooden table top"></section>
<div class="hero-products" role="img" aria-label="Green-trimmed jute tote with two brown kraft paper bags"></div>
<h1 class="hero-title">Welcome to <span>Harbourline Bag</span></h1>
<p class="hero-sub">Maecenas aliquet velit vel turpis Mauris neque metus malesuada nec ultricies sit amet porttitor</p>
<div class="search">
  <svg width="22" height="22" viewBox="0 0 24 24"><circle cx="10" cy="10" r="7" fill="none" stroke="#f26a1b" stroke-width="3"/><path d="M15 15l6 6" stroke="#f26a1b" stroke-width="3" stroke-linecap="round"/></svg>
  Enter Keyword
</div>
<div class="dots"><i></i><i class="on"></i><i></i></div>
<svg class="hero-curve" width="1200" height="90" viewBox="0 0 1200 90">
  <path d="M0 78 Q600 -30 1200 78 L1200 90 L0 90Z" fill="#6cb833"/>
  <path d="M0 92 Q600 -12 1200 92 Z" fill="#ffffff"/>
</svg>

<h2 class="section-title cat-title">Our Categories</h2>
<svg class="arrow" style="left:84px" width="24" height="44" viewBox="0 0 24 44"><path d="M22 2L3 22l19 20" fill="none" stroke="#999" stroke-width="2"/></svg>
<svg class="arrow" style="left:1082px" width="24" height="44" viewBox="0 0 24 44"><path d="M2 2l19 20L2 42" fill="none" stroke="#999" stroke-width="2"/></svg>

<div class="cat-card" style="left:134px;top:847px">
  <div class="cat-photo" style="background:linear-gradient(#b58a62,#8a6242)" role="img" aria-label="Brown kraft paper bag with twisted handles"></div>
  <div class="cat-label is-green">Kraft Bags</div>
</div>
<div class="cat-card" style="left:368px;top:876px">
  <div class="cat-photo" style="background:linear-gradient(#f2f2f2,#c9cdd2)" role="img" aria-label="White laminated gift bag with rope handles"></div>
  <div class="cat-label is-orange">Laminated bags</div>
</div>
<div class="cat-card" style="left:606px;top:855px">
  <div class="cat-photo" style="background:linear-gradient(120deg,#c8202a,#1d3c9c 60%,#222)" role="img" aria-label="Red, blue and black non-woven tote bags"></div>
  <div class="cat-label is-green">Non-woven bags</div>
</div>
<div class="cat-card" style="left:840px;top:884px">
  <div class="cat-photo" style="background:linear-gradient(#f4f2ee,#dcd8d0)" role="img" aria-label="Plain calico tote bag"></div>
  <div class="cat-label is-orange">Calico bags</div>
</div>

<svg class="about-shape" width="1200" height="460" viewBox="0 0 1200 460">
  <defs>
    <linearGradient id="aboutFill" x1="0" y1="0" x2="1" y2="0.3">
      <stop offset="0" stop-color="#f28a3a"/>
      <stop offset="1" stop-color="#e8401a"/>
    </linearGradient>
  </defs>
  <path d="M0 80 Q650 -60 1200 60 L1200 410 Q800 480 0 400 Z" fill="#6cb833"/>
  <path d="M0 95 Q650 -40 1200 78 L1200 392 Q800 462 0 382 Z" fill="url(#aboutFill)"/>
</svg>
<h2 class="section-title about-title">About Harbourline Bag</h2>
<p class="about-text" style="top:1340px">Morbi ornare gravida elit Integer congue augue et malesuada iaculis ipsum dui aliquet felis at cursus magna nisl nec elit Donec iaculis diam</p>
<p class="about-text" style="top:1406px">A nisi accumsan viverra Duis sed tellus et tortor vestibulum gravida Praesent elementum elit at tellus Curabitur metus ipsum luctus eu malesuada ut tincidunt sed diam Donec quis mi sed magna hendrerit accumsan Suspendisse risu</p>
<div class="pill-btn" style="left:425px;top:1528px;width:169px">Free Sample</div>

<h2 class="section-title gallery-title">Our Gallery</h2>
<div class="g-card g-wide" style="left:178px;top:1796px;width:418px;height:262px">
  <div class="g-title">Bag Title here</div>
  <p class="g-text">Anec quis mi sed magna hendrerit accumsan Suspendisse risus nibh ultricies eu</p>
  <div class="g-photo" style="background:linear-gradient(#ece4d6,#cfc3ae)" role="img" aria-label="Natural calico tote bag"></div>
</div>
<div class="g-card g-wide" style="left:617px;top:1796px;width:418px;height:262px">
  <div class="g-title">Bag Title here</div>
  <p class="g-text">Anec quis mi sed magna hendrerit accumsan Suspendisse risus nibh ultricies eu</p>
  <div class="g-photo" style="right:22px;top:90px;width:150px;height:80px;background:linear-gradient(#4cc4d4,#1e8fa0)" role="img" aria-label="Flat teal gift box"></div>
</div>
<div class="g-card g-small" style="left:180px;top:2076px;width:270px;height:302px">
  <div class="g-photo" style="background:linear-gradient(#a07a56,#7a5a3c)" role="img" aria-label="Brown die-cut handle paper bag"></div>
  <div class="g-title">Bag Title here</div>
  <p class="g-text">Anec quis mi sed magna hendrerit accumsan Suspendisse</p>
</div>
<div class="g-card g-small" style="left:474px;top:2076px;width:269px;height:302px">
  <div class="g-photo" style="left:68px;top:30px;width:135px;height:140px;background:linear-gradient(#9c7050,#6a4a30)" role="img" aria-label="Brown kraft cardboard box"></div>
  <div class="g-title">Bag Title here</div>
  <p class="g-text">Anec quis mi sed magna hendrerit accumsan Suspendisse</p>
</div>
<div class="g-card g-small" style="left:767px;top:2076px;width:270px;height:302px">
  <div class="g-photo" style="background:linear-gradient(#e8c233,#c99a10)" role="img" aria-label="Yellow paper bag with white handles"></div>
  <div class="g-title">Bag Title here</div>
  <p class="g-text">Anec quis mi sed magna hendrerit accumsan Suspendisse</p>
</div>
<div class="pill-btn" style="left:520px;top:2406px;width:168px">View More</div>

<footer class="site-footer"></footer>
<div class="footer-brand">Harbourline<br>Bag</div>
<div class="f-col f-contact" style="left:406px">
  <h4>CONTACT US</h4>
  <ul><li>PO Box 218, Kelso Vic, 3870.</li><li>ABN: 52 904 316 281</li><li>Call 1300 482 615</li></ul>
</div>
<div class="f-col" style="left:646px">
  <h4>COMPANY</h4>
  <ul><li>Home</li><li>About us</li><li>Gallery</li><li>Bag Size</li><li>Contact us</li></ul>
</div>
<div class="f-col" style="left:767px">
  <h4>RESOURCES</h4>
  <ul><li>Kraft Paper Bags</li><li>Laminated bags</li><li>Non-woven bags</li><li>Calico bags</li><li>View all</li></ul>
</div>
<div class="f-col social" style="left:912px">
  <h4>GET IN TOUCH</h4>
  <ul><li><i></i>Chirpline</li><li><i></i>Friendbook</li><li><i></i>WorkLink</li><li><i></i>Snapgram</li></ul>
</div>
<div class="copyright">Copyright © 2019 All right reserved</div>

</body>
</html>
```